Bright Start Services (special education services) needs a Brochure Design

We need a brochure design for a new company. We are an Bright Start Services providing special education, speech, occupational and physical therapy to children birth - 3 years of age. The children we provide services for have a wide range of disabilities. Please include some stock photos if possible. Brochure text is attached.
Updates

Project Deadline Extended Reason: 1. We would like to see pictures that are multicultural (not all Caucasian).2. Some of the pictures (which were taken from our website) that were used by designers are of children that are older than 3 yrs. Please use new/different pictures of children birth-3 yrs. 3. Update the text that is in the brochure. Original line is: "The Bright Start Services (BSS) is a statewide public program for infants and toddlers with special needs". Replace with "The Bright Start Services (BSS) is a statewide public program for infants and toddlers, ages birth to 3 years, with special needs". Added Monday, February 6, 2017

Target Market(s)

Parents, Doctors, Daycare Providers

Industry/Entity Type

Education

Font styles to use
Serif
Sans Serif

Requirements
Must have
• A balance between professional looking, while child friendly and colorful
Nice to have
• A few stock pictures of children (birth-age 3)

```html
<!DOCTYPE html>
<html lang="en">
<head>
<meta charset="utf-8">
<title>Bright Start Services Brochure</title>
<link href="https://fonts.googleapis.com/css2?family=Cinzel:wght@400;700&family=Source+Sans+3:wght@400;600;700&display=swap" rel="stylesheet">
<style>
:root{
  --bg:#f5f5f5;
  --paper:#f1efe9;
  --ink:#2a2a2a;
  --purple:#7a2b8f;
  --purple-deep:#5b2a86;
  --magenta:#8e2a8f;
  --orange:#e8561c;
  --white:#ffffff;
}
*{margin:0;padding:0;box-sizing:border-box}
html,body{width:841px;height:1200px;overflow:hidden;background:var(--bg)}
body{position:relative;font-family:"Source Sans 3",Arial,sans-serif;font-weight:400;color:var(--ink)}
.sheet{position:absolute;left:106px;width:634px;height:490px;background:var(--paper);box-shadow:0 1px 4px rgba(0,0,0,.18);overflow:hidden}
.sheet--outside{top:104px}
.sheet--inside{top:610px}
.col{position:absolute;font-size:8.4px;line-height:12.8px;font-weight:400}
.col p{margin-bottom:2px}
.lead{color:var(--magenta);font-weight:600}
.tagline{color:var(--magenta);font-weight:600;text-transform:uppercase;margin-top:22px}
.hero-hand{position:absolute;left:417px;top:0;width:217px;height:256px;border-bottom-left-radius:34px;background:radial-gradient(circle at 45% 55%,#e8c9b4 0%,#d99aa3 35%,#8a4a5a 70%,#3c2a30 100%)}
.brand{position:absolute;display:flex;align-items:center;gap:6px;font-family:"Cinzel",serif;color:var(--ink)}
.brand-mark{width:16px;height:16px;border-radius:50%;background:var(--orange);flex:none}
.brand--outside{left:446px;top:272px;font-size:9px;line-height:10px}
.brand--outside .brand-name{border-left:1px solid var(--ink);padding-left:5px}
.welcome{position:absolute;left:430px;top:320px;width:190px;text-align:center;font-family:"Cinzel",serif;font-weight:700;color:var(--magenta);font-size:18px;line-height:19.5px}
.band{position:absolute;left:0;top:396px;width:634px;height:94px}
.band-text{position:absolute;color:var(--white);font-size:7px;font-weight:600;line-height:9.6px}
.social{display:inline-flex;gap:4px;vertical-align:middle}
.social span{width:6px;height:6px;border-radius:50%;background:var(--white);display:block}
.hero-kids{position:absolute;left:0;top:0;width:634px;height:200px}
.heading{color:var(--orange);font-weight:600;font-size:8.8px;margin-bottom:4px}
.list{list-style:none;font-size:8.4px;line-height:14.4px;padding-left:8px}
.list li::before{content:"• "}
.col strong{font-weight:700}
.brand--inside{position:absolute;left:470px;top:418px;width:120px;flex-direction:column;gap:4px;text-align:center;font-size:8px;line-height:9.6px}
</style>
</head>
<body>

<section class="sheet sheet--outside">
  <div class="col" style="left:26px;top:48px;width:164px">
    <p>The Bright Start Services (BSS) is a statewide public program for infants and toddlers with special needs. The Program provides many different types of early intervention services to infant and toddlers with disabilities and their families. Children with diagnosed conditions that lead to developmental delays (such as Down syndrome, cerebral palsy, autism, etc.) are eligible for the BSS. Children with no diagnosis who have delays in development may be eligible for the BSS if their delays are serious enough. In New York State, the Department of Health is the lead state agency responsible for the Bright Start Services.</p>
    <p>The early years of a child’s life are very important. During the infant and toddler years, children grow quickly and have so much to learn. Some children and families face special challenges and need extra help.</p>
    <p class="tagline">Early help does make a difference!</p>
  </div>

  <div class="col" style="left:232px;top:48px;width:160px">
    <p class="lead">Early Intervention services can help you and your family:</p>
    <p>Learn the best ways to care for your child. Support and promote your child’s development. Include your child in your family and community life.</p>
    <p class="lead">Early Intervention services can be provided anywhere in the community, including:</p>
    <p>Your home, child care center or family day care home, recreational centers, play groups, playgrounds, libraries, or any place parents and children go for fun and support. In addition, services are provided at early childhood programs and early intervention facilities and centers.</p>
    <p class="lead">As a parent, you help decide:</p>
    <p>What early intervention services your child and family need; The outcomes of early intervention that are important for your child and family; When and where your child and family will get early intervention services; Who will provide services to your child and family.</p>
  </div>

  <div class="hero-hand" role="img" aria-label="Photo of a toddler holding up a hand painted in bright rainbow colours"></div>

  <div class="brand brand--outside">
    <span class="brand-mark"></span>
    <span class="brand-name">Little Steps<br>Family Center</span>
  </div>

  <h1 class="welcome">Welcome to<br>Bright Start<br>Services</h1>

  <svg class="band" viewBox="0 0 634 94" aria-hidden="true">
    <defs>
      <linearGradient id="bandFill" x1="0" y1="0" x2="0" y2="1">
        <stop offset="0" stop-color="#8a3aa0"/>
        <stop offset="1" stop-color="#5e2a88"/>
      </linearGradient>
    </defs>
    <path d="M0,2 C160,14 300,-4 420,6 S560,10 634,-2 L634,94 L0,94Z" fill="#e4dde8"/>
    <path d="M0,8 C140,26 260,-2 380,14 S560,22 634,2 L634,94 L0,94Z" fill="url(#bandFill)"/>
  </svg>

  <div class="band-text" style="left:26px;top:465px">www.littlestepskids.org</div>
  <div class="band-text" style="left:146px;top:465px"><span class="social"><span></span><span></span><span></span></span></div>
  <div class="band-text" style="left:232px;top:436px;width:160px;text-align:center">Phone: (555) 214-3090<br>Fax: (555) 214-3091<br><span style="display:block;height:3px"></span>Administrative Office: 120 Maple Avenue,<br>Riverton, NY 10001</div>
  <div class="band-text" style="left:460px;top:452px;width:130px;text-align:center">www.littlestepskids.org<br><span class="social"><span></span><span></span><span></span></span></div>
</section>

<section class="sheet sheet--inside">
  <svg class="hero-kids" viewBox="0 0 634 200" role="img" aria-label="Photo of a group of young children gathered around an adult reading a picture book">
    <defs>
      <linearGradient id="kidsFill" x1="0" y1="0" x2="1" y2="1">
        <stop offset="0" stop-color="#c9a48c"/>
        <stop offset=".45" stop-color="#7f8fa8"/>
        <stop offset="1" stop-color="#b9a89a"/>
      </linearGradient>
    </defs>
    <path d="M0,0 H634 V178 C600,196 560,188 520,182 C460,172 420,186 360,184 C300,182 250,170 190,178 C120,186 60,176 0,190Z" fill="url(#kidsFill)"/>
    <path d="M0,190 C60,176 120,186 190,178 C250,170 300,182 360,184 C420,186 460,172 520,182 C560,188 600,196 634,178" fill="none" stroke="var(--orange)" stroke-width="1.6"/>
  </svg>

  <div class="col" style="left:37px;top:216px;width:180px">
    <h2 class="heading">Services Provided</h2>
    <ul class="list">
      <li>ABA (Applied Behavior Analysis)</li>
      <li>Special Education/Instruction</li>
      <li>Speech Therapy</li>
      <li>Occupational Therapy</li>
      <li>Physical Therapy</li>
      <li>Family Training</li>
      <li>Social Work</li>
    </ul>
    <h2 class="heading" style="margin-top:24px">Evaluations Conducted</h2>
    <ul class="list">
      <li>Developmental / Cognitive</li>
      <li>Psychological</li>
      <li>Speech Therapy</li>
      <li>Occupational Therapy</li>
      <li>Physical Therapy</li>
      <li>Feeding Therapy</li>
    </ul>
  </div>

  <div class="col" style="left:242px;top:208px;width:164px">
    <h2 class="heading">Referrals</h2>
    <p>If you have concerns about your child’s development, you can call your county’s Bright Start Services to refer your child (please see your county’s number listed below). <strong>Little Steps Family Center can help you make the referral to Bright Start Services if you wish.</strong> If your child is found to be eligible for services by someone approved to perform this evaluation, you, county staff, and other team members will make a plan to help your child – and your family.</p>
    <p>Early intervention services in your plan and authorized by the county are provided at no cost to you. The county will arrange for the services to be provided and will choose the provider based on the needs of your child and family. Your child’s health insurance may</p>
  </div>

  <div class="col" style="left:451px;top:226px;width:160px">
    <p>be used to cover some of the costs. All other costs for BSS services are paid for by your county and New York State.</p>
    <p>Early intervention services are provided where it’s best for the child – in places such as your home, daycare, or other community settings. The BSS covers the cost of early intervention services only. The BSS does not pay for day care or other fees charged by community settings.</p>
    <p style="margin-top:8px">Referrals:<br>Nassau County: (555) 310-4420<br>Suffolk County: (555) 310-5530<br>NYC: (555) 310-6640</p>
  </div>

  <div class="brand brand--inside">
    <span class="brand-mark"></span>
    <span class="brand-name">Little Steps<br>Family Center</span>
  </div>
</section>

</body>
</html>
```